Flyer-Design für Handelsfirma für Afro Kosmetik
Zielgruppe
Wir sind eine Handelsfirma für Afro Kosmetik und für Frauen mit lockigen Haaren. Zur Eröffnung unseres Stores suchen wir einen Flyer, der die Zielgruppe informiert
Aufgabenstellung
Der Flyer soll unterschiedliche und austauschbare Bilder auf der ersten Seite haben. Dabei soll es sich immer um ein Hauptbild handeln, dass die entsprechende Zielgruppe anspricht. Bild 1 = Afrikaner; Bild 2 weiße mit lockigem Haar, Bild 3 = Südländer oder Latinos mit dunklem lockigem Haar.. Der Flyer soll 2 Seiten haben und in DIN LANG sein. Auf der Rückseite des Flyers soll unser Standort mit einer Karte und Wegbeschreibung sein.

```html
<!DOCTYPE html>
<html lang="de">
<head>
<meta charset="utf-8">
<title>Lina-Kibali – Neueröffnung Flyer</title>
<link href="https://fonts.googleapis.com/css2?family=Montserrat:wght@400;600;800&display=swap" rel="stylesheet">
<style>
  :root {
    --stage: #dcdbe0;
    --cream: #efede6;
    --ink: #1b1b1b;
    --white: #f7f6f2;
    --photo-rose: #a06a6e;
    --photo-blue: #a9c8de;
    --photo-dark: #3b4150;
    --photo-red: #b8523c;
    --photo-violet: #8a3f9a;
  }
  * { box-sizing: border-box; margin: 0; padding: 0; }
  html, body { width: 1200px; height: 857px; overflow: hidden; }
  body {
    background: var(--stage);
    font-family: "Montserrat", sans-serif;
    position: relative;
  }
  .flyer {
    position: absolute;
    top: 66px;
    width: 340px;
    height: 725px;
    overflow: hidden;
    box-shadow: 0 6px 18px rgba(0,0,0,.18);
  }
  .flyer--light { left: 190px; background: var(--cream); color: var(--ink); }
  .flyer--dark  { left: 670px; background: var(--ink); color: var(--white); }

  .brand { position: absolute; top: 34px; left: 0; right: 0; text-align: center; }
  .brand__name { font-size: 34px; font-weight: 400; letter-spacing: 1px; }
  .brand__tagline { margin-top: 8px; font-size: 10.5px; letter-spacing: 1.6px; font-weight: 400; }
  .brand__tagline strong { font-weight: 800; }

  .photo { position: absolute; }
  .flyer--light .photo--main { left: 22px; top: 140px; width: 168px; height: 530px;
    background: linear-gradient(180deg, #b67aa0 0%, var(--photo-rose) 30%, #5a3a30 70%, #2a2224 100%); }
  .flyer--light .photo--side { left: 198px; top: 112px; width: 120px; height: 460px;
    background: linear-gradient(180deg, #5f6a4c 0%, #4b382e 30%, var(--photo-blue) 55%, #8fb6d4 100%); }
  .flyer--dark .photo--main { left: 22px; top: 118px; width: 168px; height: 475px;
    background: linear-gradient(180deg, #2a3142 0%, #6b5648 40%, #8a6a55 65%, var(--photo-violet) 100%); }
  .flyer--dark .photo--side { left: 198px; top: 95px; width: 120px; height: 450px;
    background: linear-gradient(180deg, #9fb09a 0%, #a77d62 35%, #c48a6c 55%, var(--photo-red) 100%); }

  .opening {
    position: absolute; left: 0; right: 0; top: 500px; height: 100px;
    padding: 14px 22px 0;
  }
  .flyer--light .opening { background: var(--ink); color: var(--white); }
  .flyer--dark .opening  { background: var(--white); color: var(--ink); top: 470px; }
  .opening__title { font-size: 30px; font-weight: 800; letter-spacing: 1px; text-align: center; }
  .opening__date { font-size: 19px; font-weight: 400; letter-spacing: 1.5px; text-align: center; margin-top: 2px; }
  .opening__meta { display: flex; justify-content: space-between; font-size: 9.5px; margin-top: 8px; padding: 0 4px; }

  .website {
    position: absolute; left: 0; right: 0; bottom: 24px;
    text-align: center; font-size: 13px; letter-spacing: 1px;
  }
</style>
</head>
<body>

<section class="flyer flyer--light">
  <header class="brand">
    <div class="brand__name">Lina-Kibali</div>
    <div class="brand__tagline">MODE &amp; KOSMETIK FÜR <strong>LOCKEN</strong></div>
  </header>
  <div class="photo photo--main" role="img" aria-label="Porträt einer Frau mit dunklen Locken vor blühenden Sträuchern"></div>
  <div class="photo photo--side" role="img" aria-label="Frau mit dunklen Locken im hellblauen Top"></div>
  <div class="opening">
    <div class="opening__title">NEUERÖFFNUNG</div>
    <div class="opening__date">01.09.2020 • BONN</div>
    <div class="opening__meta"><span>ab 10 Uhr</span><span>Lindenweg 14</span></div>
  </div>
  <div class="website">www.lina-kibali.de</div>
</section>

<section class="flyer flyer--dark">
  <header class="brand">
    <div class="brand__name">Lina-Kibali</div>
    <div class="brand__tagline">MODE &amp; KOSMETIK FÜR <strong>LOCKEN</strong></div>
  </header>
  <div class="photo photo--main" role="img" aria-label="Lachendes Kind mit lockigem Haar"></div>
  <div class="photo photo--side" role="img" aria-label="Lächelndes Mädchen mit hellbraunen Locken im roten Shirt"></div>
  <div class="opening">
    <div class="opening__title">NEUERÖFFNUNG</div>
    <div class="opening__date">01.09.2020 • BONN</div>
    <div class="opening__meta"><span>ab 10 Uhr</span><span>Lindenweg 14</span></div>
  </div>
  <div class="website">www.lina-kibali.de</div>
</section>

</body>
</html>
```